Verdant Loop Advisors, LLC

I am looking for a simple, clear layout with my logo prominent and embossed, on the best quality card stock available. I would like the business name and phone number included on the card as well......I dont want my name anywhere on the card and I would like my logo embossed on the card......something simple with a white back......open to designs as long as they go along with recycling symbols and green type stuff.....The address, website, cell number, fax number, and email are listed below

5374 Tillbury Fenwood Road
Larkmoor, MD 20911

c. 240.555.0143 f. 240.555.0187
e. sales@verdantloopadvisors.example
w. www.verdantloopadvisors.example

Industry/Entity Type

Recycling

```html
<!DOCTYPE html>
<html lang="en">
<head>
<meta charset="utf-8">
<title>Verdant Loop Advisors, LLC – Business Card</title>
<link rel="stylesheet" href="https://fonts.googleapis.com/css2?family=Orbitron:wght@800&family=Quicksand:wght@500&display=swap">
<style>
  :root {
    --card-white: #f4f4f2;
    --brand-green: #1f6a3a;
    --rule-grey: #cfd3cf;
    --ink-green: #236b3c;
  }
  html, body {
    margin: 0;
    padding: 0;
    width: 1200px;
    height: 685px;
    overflow: hidden;
    background: var(--card-white);
  }
  .card {
    position: relative;
    width: 1200px;
    height: 685px;
    background: var(--card-white);
    color: var(--ink-green);
  }
  .company-name {
    position: absolute;
    left: 137px;
    top: 200px;
    margin: 0;
    font-family: "Orbitron", sans-serif;
    font-weight: 800;
    color: var(--brand-green);
    line-height: 1;
    white-space: nowrap;
  }
  .company-name .primary {
    display: block;
    font-size: 46px;
    letter-spacing: 4px;
  }
  .company-name .secondary {
    display: block;
    margin-top: 12px;
    font-size: 18px;
    letter-spacing: 26px;
  }
  .address {
    position: absolute;
    left: 140px;
    top: 310px;
    display: flex;
    gap: 20px;
    font-family: "Quicksand", sans-serif;
    font-weight: 500;
    font-size: 25px;
    line-height: 34px;
    font-style: normal;
    white-space: nowrap;
  }
  .address .pin { margin-top: 6px; flex: none; }
  .address-rule {
    position: absolute;
    left: 137px;
    top: 381px;
    width: 423px;
    height: 1px;
    background: var(--rule-grey);
  }
  .contact {
    position: absolute;
    left: 137px;
    top: 390px;
    margin: 0;
    padding: 0;
    list-style: none;
    font-family: "Quicksand", sans-serif;
    font-weight: 500;
    font-size: 25px;
    line-height: 32.5px;
    white-space: nowrap;
  }
  .contact .sep { margin: 0 16px; }
  .divider {
    position: absolute;
    left: 677px;
    top: 157px;
    width: 1px;
    height: 370px;
    background: var(--rule-grey);
  }
  .brand-mark {
    position: absolute;
    left: 678px;
    top: 200px;
    width: 522px;
    height: 290px;
    display: flex;
    align-items: center;
    justify-content: center;
    font-family: "Orbitron", sans-serif;
    font-weight: 800;
    font-size: 34px;
    letter-spacing: 1px;
    color: var(--brand-green);
  }
</style>
</head>
<body>
  <main class="card">
    <h1 class="company-name">
      <span class="primary">VERDANT LOOP</span>
      <span class="secondary">ADVISORS LLC</span>
    </h1>

    <address class="address">
      <svg class="pin" width="20" height="30" viewBox="0 0 20 30" aria-hidden="true">
        <path d="M10 0C4.5 0 0 4.4 0 9.8 0 16.5 10 30 10 30s10-13.5 10-20.2C20 4.4 15.5 0 10 0zm0 13.6a3.8 3.8 0 1 1 0-7.6 3.8 3.8 0 0 1 0 7.6z" fill="var(--brand-green)"/>
      </svg>
      <span>5374 Tillbury Fenwood Road<br>Larkmoor, MD 20911</span>
    </address>

    <div class="address-rule"></div>

    <ul class="contact">
      <li>c. 240.555.0143<span class="sep">|</span>f. 240.555.0187</li>
      <li>e. sales@verdantloopadvisors.example</li>
      <li>www.verdantloopadvisors.example</li>
    </ul>

    <div class="divider"></div>

    <div class="brand-mark">VERDANT LOOP</div>
  </main>
</body>
</html>
```